Banner ad design for Vantora Display Ads

We are looking for a designer to develop a concept for banner ads for a Vantora Display campaign we are building.

We have 3 business lines, shredding services, records management services and scanning services.

We are looking for 4 sets of ads to be created, one for each business line + one set that showcases all of our lines together.

For the design concepts, we would like to see a few sizes (banner, square, leaderboard, skyscraper, etc) for each.

The person chosen will then need to create the ads into all Vantora supported sizes -- 20 sizes total for each set of ads as per the Vantora size guidelines found on this page - https://help.vantora-example.com/vantora-ads/answer/4827150?hl=en&ref_topic=6604821#

A few items to note:
- Design should complement our existing brand/website look and feel (www.oak-ferry.ca)
- Each final ad must be 150Kb or less in size
- Final designs should be editable, meaning if we would like to change some copy in the design, we can do so using a well-known software (Canva, Photoshop/InDesign, etc)
- Some images are attached for use, but if you feel a different stock image is more suitable to to your design, please go ahead and use it.

Provided below is some messaging that can be used for each set of ads. Do not feel you need to use all of the messaging, it is provided for guidance.

SHREDDING SERVICES:

Possible Short Headline:
-- One-Time Shredding Services
-- Secure Shredding Services
-- Affordable On-Site Shredding

Possible Long Headline
-- Your Paper Can be Destroyed as Soon as the Next Business Day

Possible Descriptions:
-- KVEC Gold Certified On site shredding company. Service as soon as Next Day.
-- Secure and Affordable Toronto & GTA On-Site Shredding.
-- Certified, Affordable Office Shredding Since 2003.
-- Quick, no contact and affordable paper shredding services in Toronto & Southern Ontario.
-- Certified, Affordable Office Shredding Since 2003. Fast, no contact shredding service.

Call to Action
-- Get a Quote

RECORDS MANAGEMENT
Short Headline:
-- Off-site Records Storage
-- Records Management & Storage
-- Secure Records Storage
-- Records Management Services
-- Long Term Records Management
-- Document Storage Solutions

Possible Description
-- Local, Affordable Storage Solutions. Protect and Store your Documents in our Secure Facility
-- Local, Affordable Records Management Solutions. Store your Records in our Secure Facility
-- Certified, Affordable Document Storage Since 2004. Contact Us for a Free Quote!
-- Vaultline+ Certified, Affordable Document Storage Since 2004. Contact Us for a Free Quote!

Call to Action
-- Get a Quote

SCANNING SERVICES

Short Headline:
-- Professional Scanning Company
-- Toronto & GTA Scanning Service
-- Document Scanning Services
-- Digital Conversion Services
-- Fast & Easy Retrieval

Description
-- Scan and documents and files with Professional scanning services from Oak-Ferry
-- Convert Your Paper Files to Electronic Files. Fast & Easy Retrieval.
-- Easily access your documents electronically with Document Scanning Services

Call to Action
-- Get a Quote

ALL SERVICES AD SET
Short Headline
-- Shred, Scan & Store Documents
-- Secure Shredding, Records Management and Scanning Services
-- #1 Document Management Company
-- Oak Ferry Shredding, Storage & Scanning

Description
-- Secure and Affordable Toronto & GTA On-Site Shredding, Document Storage & Scanning Company

Call to Action
-- Get a Quote

Font styles to use
Sans Serif

```html
<!DOCTYPE html>
<html lang="en">
<head>
<meta charset="utf-8">
<title>Oak Ferry – All Services Display Ads</title>
<link rel="stylesheet" href="https://fonts.googleapis.com/css2?family=Poppins:ital,wght@0,400;0,500;0,600;0,800;1,600&family=Montserrat:wght@800&display=swap">
<style>
  :root {
    --board-bg: #d6d6d6;
    --label: #9a9a9a;
    --heading-muted: #bcbcbc;
    --ink: #232323;
    --white: #ffffff;
    --blue-deep: #1b96e4;
    --blue-bright: #2fd2ff;
    --button-bg: #242424;
    --button-ring: #84dbff;
    --paper-light: #fbfbfb;
    --paper-shade: #c9ccd1;
  }
  * { box-sizing: border-box; margin: 0; padding: 0; }
  html, body { width: 1038px; height: 1200px; overflow: hidden; }
  body { background: var(--board-bg); font-family: "Poppins", sans-serif; position: relative; }

  .format-label { position: absolute; font-size: 17px; font-weight: 500; color: var(--label); letter-spacing: .3px; }

  .ad { position: absolute; background: var(--white); overflow: hidden; box-shadow: 0 3px 7px rgba(0,0,0,.22); }
  .ad-shape { position: absolute; inset: 0; width: 100%; height: 100%; }

  .brand { position: absolute; font-weight: 600; color: var(--ink); line-height: 1; letter-spacing: -.3px; }
  .tagline { position: absolute; color: var(--ink); font-weight: 400; }
  .pitch { position: absolute; color: var(--white); font-style: italic; font-weight: 600; }

  .paper-stack {
    position: absolute; border-radius: 3px;
    background: linear-gradient(170deg, var(--paper-light) 0%, #eef0f2 55%, var(--paper-shade) 100%);
    box-shadow: 0 4px 8px rgba(0,40,80,.25);
  }

  .cta {
    position: absolute; display: flex; align-items: center; justify-content: center;
    background: var(--button-bg); color: var(--white); border: 2px solid var(--button-ring);
    border-radius: 40px; font-weight: 800; text-transform: uppercase; letter-spacing: -.2px; white-space: nowrap;
  }

  .set-title { position: absolute; left: 341px; top: 910px; font-family: "Montserrat", sans-serif; font-weight: 800; font-size: 47px; color: var(--heading-muted); letter-spacing: .5px; }
  .set-note { position: absolute; left: 344px; top: 984px; width: 520px; font-size: 15px; line-height: 26px; color: var(--label); }
</style>
</head>
<body>

  <!-- Banner -->
  <div class="format-label" style="left:110px; top:74px;">Banner</div>
  <div class="ad ad--banner" style="left:110px; top:106px; width:542px; height:69px;">
    <svg class="ad-shape" viewBox="0 0 542 69" preserveAspectRatio="none" aria-hidden="true">
      <defs>
        <linearGradient id="banner-blue" x1="0" y1="0" x2="1" y2="1">
          <stop offset="0" stop-color="var(--blue-deep)"/><stop offset="1" stop-color="var(--blue-bright)"/>
        </linearGradient>
      </defs>
      <path d="M200 0 L542 0 L542 69 L168 69 C170 32 182 10 200 0 Z" fill="var(--ink)"/>
      <path d="M212 0 L542 0 L542 69 L180 69 C184 34 194 12 212 0 Z" fill="url(#banner-blue)"/>
    </svg>
    <div class="brand" style="left:28px; top:15px; font-size:21px;">oak ferry</div>
    <div class="tagline" style="left:28px; top:41px; font-size:9px;">Shredding, Storage &amp; Scanning</div>
    <div class="pitch" style="left:194px; top:13px; width:140px; font-size:9px; line-height:11px;">Quick, no contact and affordable paper shredding services in Toronto &amp; Southern Ontario.</div>
    <div class="paper-stack" role="img" aria-label="Stack of white paper" style="left:338px; top:12px; width:88px; height:42px;"></div>
    <div class="cta" style="left:433px; top:18px; width:94px; height:33px; font-size:8px;">Get a quote</div>
  </div>

  <!-- Leaderboard -->
  <div class="format-label" style="left:110px; top:218px;">Leaderboard</div>
  <div class="ad ad--leaderboard" style="left:110px; top:248px; width:841px; height:104px;">
    <svg class="ad-shape" viewBox="0 0 841 104" preserveAspectRatio="none" aria-hidden="true">
      <defs>
        <linearGradient id="leader-blue" x1="0" y1="0" x2="1" y2="1">
          <stop offset="0" stop-color="var(--blue-deep)"/><stop offset="1" stop-color="var(--blue-bright)"/>
        </linearGradient>
      </defs>
      <path d="M290 0 L841 0 L841 104 L250 104 C252 50 266 16 290 0 Z" fill="var(--ink)"/>
      <path d="M306 0 L841 0 L841 104 L266 104 C270 52 282 18 306 0 Z" fill="url(#leader-blue)"/>
    </svg>
    <div class="brand" style="left:28px; top:22px; font-size:34px;">oak ferry</div>
    <div class="tagline" style="left:28px; top:63px; font-size:13px;">Shredding, Storage &amp; Scanning</div>
    <div class="pitch" style="left:296px; top:23px; width:205px; font-size:12.5px; line-height:16px;">Quick, no contact and affordable paper shredding services in Toronto &amp; Southern Ontario.</div>
    <div class="paper-stack" role="img" aria-label="Stack of white paper" style="left:512px; top:14px; width:162px; height:78px;"></div>
    <div class="cta" style="left:696px; top:31px; width:120px; height:40px; font-size:11px;">Get a quote</div>
  </div>

  <!-- Skyscraper -->
  <div class="format-label" style="left:110px; top:397px;">Skyscraper</div>
  <div class="ad ad--skyscraper" style="left:110px; top:426px; width:139px; height:693px;">
    <svg class="ad-shape" viewBox="0 0 139 693" preserveAspectRatio="none" aria-hidden="true">
      <defs>
        <linearGradient id="sky-blue" x1="0" y1="0" x2="0" y2="1">
          <stop offset="0" stop-color="var(--blue-deep)"/>
          <stop offset=".62" stop-color="var(--blue-bright)"/>
          <stop offset="1" stop-color="var(--blue-deep)"/>
        </linearGradient>
      </defs>
      <path d="M0 180 C40 160 105 168 139 222 L139 693 L0 693 Z" fill="var(--ink)"/>
      <path d="M0 200 C48 182 115 196 139 268 L139 693 L0 693 Z" fill="url(#sky-blue)"/>
    </svg>
    <div class="brand" style="left:22px; top:20px; font-size:32px; line-height:32px;">oak<br>ferry</div>
    <div class="tagline" style="left:22px; top:101px; font-size:13px; line-height:17px;">Shredding,<br>Storage &amp;<br>Scanning</div>
    <div class="pitch" style="left:17px; top:247px; width:108px; font-size:11px; line-height:16.7px;">Quick,<br>no contact<br>and affordable<br>paper<br>shredding services<br>in Toronto<br>&amp; Southern<br>Ontario.</div>
    <div class="paper-stack" role="img" aria-label="Stack of white paper" style="left:13px; top:458px; width:115px; height:55px;"></div>
    <div class="cta" style="left:16px; top:598px; width:106px; height:37px; font-size:9px;">Get a quote</div>
  </div>

  <!-- Square -->
  <div class="format-label" style="left:336px; top:397px;">Square</div>
  <div class="ad ad--square" style="left:341px; top:426px; width:289px; height:289px;">
    <svg class="ad-shape" viewBox="0 0 289 289" preserveAspectRatio="none" aria-hidden="true">
      <defs>
        <radialGradient id="square-blue" cx=".4" cy=".9" r=".9">
          <stop offset="0" stop-color="var(--blue-bright)"/><stop offset="1" stop-color="var(--blue-deep)"/>
        </radialGradient>
      </defs>
      <path d="M0 128 C60 100 130 90 180 96 C240 104 282 170 289 240 L289 289 L0 289 Z" fill="var(--ink)"/>
      <path d="M0 140 C60 114 128 106 172 112 C228 120 268 186 276 289 L0 289 Z" fill="url(#square-blue)"/>
    </svg>
    <div class="brand" style="left:27px; top:22px; font-size:34px;">oak ferry</div>
    <div class="tagline" style="left:27px; top:60px; font-size:13px;">Shredding, Storage &amp; Scanning</div>
    <div class="pitch" style="left:28px; top:136px; width:168px; font-size:11px; line-height:14px;">Quick, no contact and affordable paper shredding services in Toronto &amp; Southern Ontario.</div>
    <div class="paper-stack" role="img" aria-label="Stack of white paper" style="left:22px; top:200px; width:138px; height:64px;"></div>
    <div class="cta" style="left:162px; top:228px; width:106px; height:36px; font-size:9px;">Get a quote</div>
  </div>

  <div class="set-title">ALL SERVICES AD</div>
  <p class="set-note">Lorem Ipsum is simply dummy text of the printing and typesetting industry. Lorem Ipsum has been.</p>

</body>
</html>
```